Healthcare IT company looking for business card design

We develop IT systems for healthcare that significantly reduces cost and improves quality.

We want a business card design that is professional and clean, and using the colors in our logo.

Target Market(s)

Doctors and decision makers in the healthcare industry

Industry/Entity Type

Healthcare

Contact Information for Business Card

It should include
Name and title, address, telephone

Tobias Vrenholt, CEO
+46 712 418257
tobias@kelvaro.se

Font styles to use
Serif

Colors
0355a3
ed282f

Requirements
Must have
• Clean design
• Professional feel
Nice to have
• N/A
Should not have
• N/A

```html
<!DOCTYPE html>
<html lang="en">
<head>
<meta charset="utf-8">
<title>Kelvaro business card</title>
<link rel="stylesheet" href="https://fonts.googleapis.com/css2?family=Open+Sans:wght@400;600;700&display=swap">
<style>
  :root {
    --brand-blue: #0355a3;
    --brand-red: #c8191f;
    --accent-red: #ed282f;
    --paper: #eeeff1;
    --ink: #4a4a4a;
    --backdrop: #e4e4e4;
  }
  * { box-sizing: border-box; margin: 0; padding: 0; }
  html, body {
    width: 1105px;
    height: 1200px;
    overflow: hidden;
    background: var(--backdrop);
    font-family: "Open Sans", Arial, sans-serif;
  }
  .canvas { position: relative; width: 1105px; height: 1200px; }

  .card {
    position: absolute;
    left: 180px;
    width: 746px;
    height: 426px;
  }
  .card-front { top: 119px; background: var(--paper); }
  .card-back { top: 637px; background: var(--brand-red); }

  /* front */
  .name-band {
    position: absolute;
    left: 0; top: 51px;
    width: 416px; height: 68px;
    background: var(--brand-blue);
    color: #fff;
    padding: 4px 0 0 36px;
  }
  .holder-name { font-size: 26px; font-weight: 600; line-height: 34px; }
  .holder-title { font-size: 19px; font-weight: 400; line-height: 24px; }

  .wordmark {
    position: absolute;
    left: 424px; top: 44px;
    display: flex; align-items: center; gap: 10px;
  }
  .wordmark-name {
    font-size: 64px; font-weight: 700;
    color: var(--brand-blue);
    line-height: 80px;
    letter-spacing: -1px;
  }
  .wordmark-dot {
    width: 18px; height: 18px;
    border-radius: 50%;
    background: var(--accent-red);
    margin-top: -38px;
  }

  .contact-list {
    position: absolute;
    left: 38px; top: 300px;
    list-style: none;
  }
  .contact-item {
    display: flex; align-items: center; gap: 12px;
    height: 29px;
    font-size: 18px; color: var(--ink);
  }
  .contact-icon { width: 18px; height: 18px; flex: none; }

  .address {
    position: absolute;
    right: 43px; top: 330px;
    text-align: right;
    font-style: normal;
    font-size: 18px; line-height: 26px;
    color: var(--ink);
  }

  /* back */
  .back-wordmark {
    position: absolute;
    left: 0; right: 0; top: 160px;
    text-align: center;
    font-size: 76px; font-weight: 700;
    color: var(--paper);
    line-height: 96px;
    letter-spacing: -1px;
  }
  .back-url {
    position: absolute;
    left: 0; right: 0; top: 354px;
    text-align: center;
    font-size: 20px; font-style: italic;
    letter-spacing: 9px;
    color: var(--paper);
  }
</style>
</head>
<body>
<main class="canvas">
  <section class="card card-front" aria-label="Business card front">
    <div class="name-band">
      <p class="holder-name">Tobias Vrenholt</p>
      <p class="holder-title">CEO</p>
    </div>
    <div class="wordmark">
      <span class="wordmark-name">Kelvaro</span>
      <span class="wordmark-dot"></span>
    </div>
    <ul class="contact-list">
      <li class="contact-item">
        <svg class="contact-icon" viewBox="0 0 24 24" aria-hidden="true"><path fill="#0355a3" d="M6.6 10.8a15.2 15.2 0 0 0 6.6 6.6l2.2-2.2c.3-.3.7-.4 1-.2 1.1.4 2.3.6 3.6.6.6 0 1 .4 1 1V20c0 .6-.4 1-1 1A17 17 0 0 1 3 4c0-.6.4-1 1-1h3.5c.6 0 1 .4 1 1 0 1.3.2 2.5.6 3.6.1.3 0 .7-.2 1z"/></svg>
        <span>+46 712 418257</span>
      </li>
      <li class="contact-item">
        <svg class="contact-icon" viewBox="0 0 24 24" aria-hidden="true"><rect x="2" y="5" width="20" height="14" rx="1.5" fill="#0355a3"/><path d="M3 6.5l9 6.5 9-6.5" fill="none" stroke="#eeeff1" stroke-width="1.8"/></svg>
        <span>tobias@kelvaro.se</span>
      </li>
      <li class="contact-item">
        <svg class="contact-icon" viewBox="0 0 24 24" aria-hidden="true"><circle cx="12" cy="12" r="10" fill="#0355a3"/><path d="M2 12h20M12 2c3 3 3 17 0 20M12 2c-3 3-3 17 0 20" fill="none" stroke="#eeeff1" stroke-width="1.3"/></svg>
        <span>www.kelvaro.se</span>
      </li>
    </ul>
    <address class="address">
      2140 Birchwood Lane<br>
      Fairbanks, Alaska 39821
    </address>
  </section>

  <section class="card card-back" aria-label="Business card back">
    <p class="back-wordmark">Kelvaro</p>
    <p class="back-url">www.kelvaro.se</p>
  </section>
</main>
</body>
</html>
```